Advertisement Design Project

SIZE 9.75" WIDTH 7" HIGHT
I ADDED LOGO,
We are fashion fabric manufacture in la ca.
we need design for our advertising in Meridian garment ledge.
size : width: 10" height 7"
half page. attached our previous ads.
our web: talin@talinworksco.com

Target Market(s)

high end designers, fashionable clothing company, contemporary marker

Industry/Entity Type

Advertising

Requirements
Must have
• look our attachments, i am not happy with our provisos ads.
Nice to have
• Meridian garment ledger wrote about us full page not as advertising,
nice to read it.
Should not have
• CONTEMPORARY CLOTHING DESIGNERS BUYING FROM US FABRIC FOR DRESSES TOPS, HIGH END

```html
<!DOCTYPE html>
<html lang="en">
<head>
<meta charset="utf-8">
<title>Talin Works Co. – Fashion Forward Fabrics</title>
<link rel="stylesheet" href="https://fonts.googleapis.com/css2?family=Questrial&display=swap">
<style>
  :root {
    --paper: #f2f2f1;
    --paper-edge: #e6e6e5;
    --brown: #3a2417;
    --green: #8cc43f;
    --grey: #979797;
    --white: #ffffff;
  }
  * { box-sizing: border-box; margin: 0; padding: 0; }
  html, body { width: 1200px; height: 840px; overflow: hidden; }
  body { font-family: "Questrial", "Century Gothic", sans-serif; }
  .ad {
    position: relative;
    width: 1200px;
    height: 840px;
    overflow: hidden;
    background: radial-gradient(ellipse at 40% 40%, var(--paper) 55%, var(--paper-edge) 100%);
  }
  .model-photo {
    position: absolute;
    left: 732px; top: 0;
    width: 468px; height: 840px;
    background:
      linear-gradient(100deg, rgba(0,0,0,0) 0%, rgba(0,0,0,0) 100%),
      linear-gradient(180deg, #dcdcdc 0%, #cfcfcf 22%, #c8234a 32%, #b0204a 55%, #7a2a8a 75%, #5b2d7e 100%);
    -webkit-mask: linear-gradient(90deg, transparent 0%, #000 8%, #000 92%, transparent 100%);
            mask: linear-gradient(90deg, transparent 0%, #000 8%, #000 92%, transparent 100%);
  }
  .brand-name {
    position: absolute;
    left: 120px; top: 104px;
    width: 520px;
    font-size: 74px;
    line-height: 1;
    letter-spacing: 4px;
    color: var(--brown);
    font-weight: 400;
    white-space: nowrap;
  }
  .values-band {
    position: absolute;
    left: 18px; top: 324px;
    width: 720px; height: 48px;
    background: var(--brown);
    color: var(--white);
    font-size: 23.5px;
    line-height: 48px;
    text-align: center;
    white-space: nowrap;
  }
  .offer {
    position: absolute;
    left: 0; top: 424px;
    width: 752px;
    text-align: center;
    color: var(--grey);
  }
  .offer-title {
    font-size: 32px;
    font-weight: 400;
    color: var(--green);
    line-height: 1;
    letter-spacing: 0.5px;
  }
  .offer-lead {
    margin-top: 12px;
    font-size: 21px;
    line-height: 1.2;
  }
  .fabric-list {
    list-style: none;
    margin-top: 10px;
    font-size: 21.5px;
    line-height: 30px;
  }
  .contact {
    position: absolute;
    top: 686px;
    color: var(--grey);
    font-size: 21px;
    line-height: 25px;
    font-style: normal;
  }
  .contact-address { left: 82px; }
  .contact-direct { left: 392px; }
  .web-bar {
    position: absolute;
    left: 116px; top: 786px;
    width: 526px; height: 54px;
    background: var(--green);
    color: var(--white);
    font-size: 29px;
    line-height: 54px;
    text-align: center;
  }
</style>
</head>
<body>
  <main class="ad">
    <div class="model-photo" role="img" aria-label="Photo of a model in a strapless fitted gown made of jewel-toned red, purple, blue and green printed fabric"></div>

    <h1 class="brand-name">TALIN WORKS co.</h1>

    <p class="values-band">Fashion - Perfection - Flexibility - Luxurious - High Quality</p>

    <section class="offer">
      <h2 class="offer-title">FASHION FORWARD</h2>
      <p class="offer-lead">Fabrics of luxurious fibers made with love in california</p>
      <ul class="fabric-list">
        <li>- Viscose Cupra - Sonora Corn Jersey</li>
        <li>- Viscose Silk Cashmere - Micro Modal Silk</li>
        <li>- Couture Italian Terry -Metallic sparkle Fleece</li>
        <li>... And Much More!</li>
      </ul>
    </section>

    <address class="contact contact-address">1840 E. 9th Street #B204<br>Fairhaven, CA 90417</address>
    <address class="contact contact-direct">T: 555 014 2736<br>sales@talinworksco.com</address>

    <p class="web-bar">www.talinworksco.com</p>
  </main>
</body>
</html>
```